Zanquerra Business Card Design

Zanquerra is a small and new restaurant/ bar location in Hong Kong. The name "Djibouti" derives from an African country. There is no specific reason behind other than the fact, that the bar is somewhat inspired by African elements (only inspired but not purely based on African cuisine etc.).

The bar is somewhat a fusion of African, Mediterranean and Oriental (Old French Vietnam) elements.

However, it is very imperative to stress, that the overall look and feel of Zanquerra is a very high end cocktail lounge/ bar location. The bar is tucked away in a hidden alley, so people will have to know about it. The idea is to send the consumer off in an Escape or hidden remote location where they are at ease in a hip, stylish and trendy environment.

The card needs to feel high-end.

Final logo artwork has been attached and also pictures of the bar/ restaurant itself. The logo ie monkey head cannot be modified. However, the background color and the color of the type "ZANQUERRA" can be changed.

The following details need to fit onto the business card. Of course they can be arranged to your liking:

LOGO

Tobin Le
Partner

+852 90817364
xxx@zanquerra-bar.com
www.zanquerra-bar.com
4C, Pelham Lane, Wan Chai, Hong Kong

Industry/Entity Type

Restaurant

```html
<!DOCTYPE html>
<html lang="en">
<head>
<meta charset="utf-8">
<title>Zanquerra Business Card</title>
<link href="https://fonts.googleapis.com/css2?family=Open+Sans:wght@400;600&display=swap" rel="stylesheet">
<style>
  :root {
    --page: #ffffff;
    --card: #1e120c;
    --ink: #f4efe9;
    --ink-soft: #d9d1c8;
    --rule: #8a7d72;
    --ghost: rgba(150, 120, 100, 0.28);
    --shadow: rgba(0, 0, 0, 0.45);
  }
  * { box-sizing: border-box; margin: 0; padding: 0; }
  html, body {
    width: 1200px; height: 533px; overflow: hidden;
    background: var(--page);
    font-family: "Open Sans", Arial, sans-serif;
  }
  .stage { position: relative; width: 1200px; height: 533px; }
  .card {
    position: absolute; top: 97px;
    width: 492px; height: 307px;
    background: var(--card);
    overflow: hidden;
    box-shadow: 10px 12px 14px var(--shadow);
  }
  .card--front { left: 59px; }
  .card--back { left: 618px; }
  .ghost-ring { position: absolute; pointer-events: none; }
  .brand-mark { position: absolute; }
  .wordmark {
    position: absolute;
    color: var(--ink);
    font-weight: 600;
    text-transform: uppercase;
    white-space: nowrap;
  }
  .card--front .wordmark {
    left: 120px; top: 136px; width: 250px; text-align: center;
    font-size: 34px; letter-spacing: 2px;
  }
  .card--back .wordmark {
    left: 282px; top: 168px; width: 150px; text-align: center;
    font-size: 19px; letter-spacing: 1px;
  }
  .contact { position: absolute; left: 42px; top: 85px; color: var(--ink); }
  .contact__name { font-size: 19px; font-weight: 600; line-height: 1; }
  .contact__role { font-size: 16px; color: var(--ink-soft); margin-top: 10px; line-height: 1; }
  .contact__address {
    font-size: 11.5px; line-height: 17px; margin: 12px 0 4px 8px; font-style: normal;
  }
  .contact__line {
    display: flex; align-items: center; gap: 6px;
    font-size: 11.5px; line-height: 18.5px;
  }
  .contact__line svg { width: 10px; height: 10px; flex: none; }
  .contact__line--web span { font-style: italic; }
  .divider {
    position: absolute; left: 255px; top: 76px;
    width: 1px; height: 174px; background: var(--rule);
  }
</style>
</head>
<body>
<main class="stage">

  <section class="card card--front" aria-label="Card front">
    <svg class="ghost-ring" style="left:222px;top:15px" width="316" height="316" viewBox="0 0 316 316" aria-hidden="true">
      <circle cx="158" cy="158" r="154" fill="none" stroke="var(--ghost)" stroke-width="4"/>
    </svg>
    <svg class="brand-mark" style="left:177px;top:56px" width="136" height="136" viewBox="0 0 136 136" aria-hidden="true">
      <circle cx="68" cy="68" r="64" fill="none" stroke="var(--ink)" stroke-width="3"/>
    </svg>
    <div class="wordmark" style="top:196px">Zanquerra</div>
  </section>

  <section class="card card--back" aria-label="Card back">
    <svg class="ghost-ring" style="left:199px;top:15px" width="316" height="316" viewBox="0 0 316 316" aria-hidden="true">
      <circle cx="158" cy="158" r="154" fill="none" stroke="var(--ghost)" stroke-width="4"/>
    </svg>

    <div class="contact">
      <p class="contact__name">Tobin Le</p>
      <p class="contact__role">Partner</p>
      <address class="contact__address">4C, Pelham Lane, Wan Chai,<br>Hong Kong</address>
      <p class="contact__line">
        <svg viewBox="0 0 10 10" aria-hidden="true"><path d="M2 0.5 L3.6 2.6 L2.8 3.6 Q4 6 6.4 7.2 L7.4 6.4 L9.5 8 L8.4 9.5 Q3.5 9 0.5 1.6 Z" fill="var(--ink)"/></svg>
        <span>+852 90817364</span>
      </p>
      <p class="contact__line">
        <svg viewBox="0 0 10 10" aria-hidden="true"><rect x="0.5" y="2" width="9" height="6" fill="none" stroke="var(--ink)" stroke-width="0.9"/><path d="M0.5 2 L5 5.6 L9.5 2" fill="none" stroke="var(--ink)" stroke-width="0.9"/></svg>
        <span>xxx@zanquerra-bar.com</span>
      </p>
      <p class="contact__line contact__line--web">
        <svg viewBox="0 0 10 10" aria-hidden="true"><circle cx="5" cy="5" r="4.4" fill="none" stroke="var(--ink)" stroke-width="0.9"/><ellipse cx="5" cy="5" rx="1.9" ry="4.4" fill="none" stroke="var(--ink)" stroke-width="0.8"/><path d="M0.6 5 H9.4" stroke="var(--ink)" stroke-width="0.8"/></svg>
        <span>www.zanquerra-bar.com</span>
      </p>
    </div>

    <div class="divider" aria-hidden="true"></div>

    <svg class="brand-mark" style="left:318px;top:110px" width="78" height="78" viewBox="0 0 78 78" aria-hidden="true">
      <circle cx="39" cy="39" r="36" fill="none" stroke="var(--ink)" stroke-width="2"/>
    </svg>
    <div class="wordmark" style="top:194px">Zanquerra</div>
  </section>

</main>
</body>
</html>
```